Brackenmoor - Healthcare Brochure - B2B

We need a new brochure design, we're satisfied with the copy but were just looking for complete overhaul of the design. Please see an example of the old design attached. It was just a template we filled out.
Requirements
Nice to have
- The second attachment is an example of a style we like

```html
<!DOCTYPE html>
<html lang="en">
<head>
<meta charset="UTF-8">
<title>Brackenmoor – Care Coordination</title>
<link href="https://fonts.googleapis.com/css2?family=Poppins:wght@400;500;600&display=swap" rel="stylesheet">
<style>
  :root {
    --brand-blue: #1779c2;
    --panel-grey: #f2f2f4;
    --ink: #1e1e1e;
    --body-ink: #3d3d3d;
    --icon-ink: #4a4a4a;
    --white: #ffffff;
  }
  * { margin: 0; padding: 0; box-sizing: border-box; }
  html, body { width: 1200px; height: 927px; overflow: hidden; background: var(--white); }
  body { font-family: "Poppins", sans-serif; color: var(--body-ink); }
  .sheet { position: relative; width: 1200px; height: 927px; overflow: hidden; background: var(--white); }

  .mission-panel { position: absolute; left: 0; top: 41px; width: 1200px; height: 440px; background: var(--panel-grey); }
  .mission { position: absolute; left: 41px; top: 134px; width: 292px; }
  .mission-title { font-weight: 500; font-size: 23px; color: var(--ink); line-height: 1.1; letter-spacing: -0.2px; }
  .mission-rule { width: 63px; height: 3px; background: var(--brand-blue); margin: 5px 0 11px; }
  .mission-text { font-size: 15.4px; line-height: 21.2px; }

  .hero-photo { position: absolute; left: 400px; top: 0; width: 715px; height: 481px;
    background: linear-gradient(100deg, #d9d5d2 0%, #e9e8ea 40%, #eef0f2 60%, #6cc3da 85%, #3fb3d3 100%); }
  .accent-block { position: absolute; left: 1010px; top: 46px; width: 190px; height: 65px; background: var(--brand-blue); }

  .process-dot { position: absolute; left: 29px; top: 472px; width: 70px; height: 70px; border-radius: 50%; background: var(--brand-blue); }
  .process-intro { position: absolute; left: 121px; top: 500px; width: 900px; font-size: 15.1px; line-height: 22px; color: var(--body-ink); }

  .service { position: absolute; width: 222px; }
  .service-icon { position: absolute; left: -70px; top: 2px; width: 38px; height: 38px; }
  .service-rule { position: absolute; left: -11px; top: -3px; width: 1.5px; height: 95px; background: var(--brand-blue); }
  .service-title { font-weight: 600; font-size: 13.8px; color: var(--ink); line-height: 18px; margin-bottom: 3px; white-space: nowrap; }
  .service-text { font-size: 13.6px; line-height: 18.2px; }

  .footer-band { position: absolute; left: 0; top: 908px; width: 1200px; height: 19px; background: var(--brand-blue); }
  svg.icon { fill: none; stroke: var(--icon-ink); stroke-width: 1.6; stroke-linecap: round; stroke-linejoin: round; }
</style>
</head>
<body>
<div class="sheet">
  <div class="mission-panel"></div>

  <section class="mission">
    <h2 class="mission-title">Our Mission</h2>
    <div class="mission-rule"></div>
    <p class="mission-text">To make the healthcare experience for every patient as fluid, efficient, and compassionate as possible. Through cutting-edge care and seamless coordination, we ensure patients recover faster, stay healthier, and never lose sight of their well-being.</p>
  </section>

  <div class="hero-photo" role="img" aria-label="Nurse in teal scrubs holding the hand of a smiling older patient resting in a hospital bed"></div>
  <div class="accent-block"></div>

  <div class="process-dot"></div>
  <p class="process-intro">Our process is quick, straightforward, and, most importantly, effective. With just one call, we handle the rest—guiding patients seamlessly from your healthcare facility to their home, ensuring support every step of the way.</p>

  <article class="service" style="left:114px; top:582px;">
    <div class="service-rule"></div>
    <svg class="icon service-icon" viewBox="0 0 40 40"><rect x="2" y="10" width="24" height="20" rx="2"/><path d="M26 16h6l6 7v7H26"/><circle cx="9" cy="32" r="2.5"/><circle cx="31" cy="32" r="2.5"/><path d="M14 14v12M8 20h12"/><path d="M30 4a6 6 0 0 1 5 5M30 8a2 2 0 0 1 2 2"/></svg>
    <h3 class="service-title">Seamless Transition</h3>
    <p class="service-text">We ensure smooth facility-to-home transitions with no gaps in care, prioritizing patient outcomes.</p>
  </article>

  <article class="service" style="left:514px; top:582px;">
    <div class="service-rule"></div>
    <svg class="icon service-icon" viewBox="0 0 40 40"><path d="M3 4v34M3 32h34M37 24v14M3 24h34"/><path d="M8 6h4v6H8z"/><path d="M10 12v8"/><circle cx="16" cy="16" r="3"/><path d="M20 20h12l3 4"/></svg>
    <h3 class="service-title">Reduced Readmission Risk</h3>
    <p class="service-text">We minimize readmission risk with proactive care, enhancing outcomes and supporting value-based care goals.</p>
  </article>

  <article class="service" style="left:914px; top:582px;">
    <div class="service-rule"></div>
    <svg class="icon service-icon" viewBox="0 0 40 40"><circle cx="7" cy="6" r="3"/><path d="M2 14a5 5 0 0 1 10 0z"/><circle cx="33" cy="6" r="3"/><path d="M28 14a5 5 0 0 1 10 0z"/><circle cx="7" cy="28" r="3"/><path d="M2 36a5 5 0 0 1 10 0z"/><circle cx="33" cy="28" r="3"/><path d="M28 36a5 5 0 0 1 10 0z"/><rect x="16" y="16" width="8" height="8"/><path d="M20 18v4M18 20h4M20 4v8M20 28v8"/></svg>
    <h3 class="service-title">Streamlined Referral Process</h3>
    <p class="service-text">Easily refer patients with a fast, simple process that ensures seamless transitions in care.</p>
  </article>

  <article class="service" style="left:114px; top:735px;">
    <div class="service-rule"></div>
    <svg class="icon service-icon" viewBox="0 0 40 40"><rect x="3" y="3" width="24" height="34" rx="2"/><path d="M8 10h14M8 15h14M8 20h12M8 25h8M8 30h6"/><rect x="28" y="24" width="8" height="13" rx="2"/><path d="M29 20h6v4h-6z"/></svg>
    <h3 class="service-title">Prescription Refills</h3>
    <p class="service-text">We handle refills for non-controlled prescriptions, ensuring your patients have what they need to recover.</p>
  </article>

  <article class="service" style="left:514px; top:735px;">
    <div class="service-rule"></div>
    <svg class="icon service-icon" viewBox="0 0 40 40"><rect x="6" y="4" width="28" height="34" rx="2"/><rect x="14" y="2" width="12" height="5" rx="1"/><path d="M11 14h18M11 20h18M11 26h10M11 31h10"/><path d="M27 25v6M24 28h6"/></svg>
    <h3 class="service-title">VNA Order Sign-Off</h3>
    <p class="service-text">We sign off on VNA orders, streamlining the process and ensuring seamless home care coordination.</p>
  </article>

  <article class="service" style="left:914px; top:735px;">
    <div class="service-rule"></div>
    <svg class="icon service-icon" viewBox="0 0 40 40"><rect x="2" y="3" width="30" height="20"/><path d="M8 10v6M5 13h6M15 10l3 3 3-5 3 4"/><circle cx="33" cy="10" r="3"/><path d="M29 22v-6h8v6"/><circle cx="6" cy="28" r="2.5"/><path d="M2 36a4 4 0 0 1 8 0M2 32h8"/><circle cx="17" cy="28" r="2.5"/><path d="M13 36a4 4 0 0 1 8 0M13 32h8"/><path d="M26 30h10M26 34h12"/></svg>
    <h3 class="service-title">Patient Education</h3>
    <p class="service-text">Empowering patient’s with information to make informed decisions about their health.</p>
  </article>

  <div class="footer-band"></div>
</div>
</body>
</html>
```